Summit Ridge Builders Business Card ideas

We want a business card to represents our company in a way that looks professional but is also a business card that is unique!

Industry/Entity Type

Construction Company

Contact Information for Business Card

open to all design ideas, just want to be able to see different options to choose from in either color or grayscale.

Requirements
Must have
• Our names and phone numbers
• Mark Halden 541-555-0142
• Derek Walsh 386-555-0187
• Business logo

```html
<!DOCTYPE html>
<html lang="en">
<head>
<meta charset="utf-8">
<title>Summit Ridge Builders – Business Card</title>
<link rel="stylesheet" href="https://fonts.googleapis.com/css2?family=Cinzel:wght@400;600&family=PT+Sans:wght@400&display=swap">
<style>
  :root {
    --backdrop: #e6e3df;
    --card-light: #ffffff;
    --card-dark: #000000;
    --ink: #1a1a1a;
    --ink-soft: #555555;
    --rule: #9a9a9a;
    --paper-text: #ffffff;
  }
  * { margin: 0; padding: 0; box-sizing: border-box; }
  html, body {
    width: 1200px; height: 987px; overflow: hidden;
    background: var(--backdrop);
  }
  .canvas { position: relative; width: 1200px; height: 987px; }
  .card {
    position: absolute; width: 615px; height: 350px;
    box-shadow: 0 2px 6px rgba(0,0,0,0.18);
  }
  .card--front { left: 293px; top: 131px; background: var(--card-light); color: var(--ink); }
  .card--back { left: 292px; top: 506px; background: var(--card-dark); color: var(--paper-text); }

  .brand {
    position: absolute; display: flex; align-items: center; gap: 12px;
    font-family: "Cinzel", serif; font-weight: 600; font-size: 25px;
    letter-spacing: 0.5px; white-space: nowrap; line-height: 1;
  }
  .brand__mark { width: 16px; height: 16px; background: currentColor; flex: none; }
  .card--front .brand { right: 41px; top: 76px; color: var(--ink); }
  .card--back .brand { left: 0; right: 0; justify-content: center; top: 170px; }

  .person { position: absolute; left: 33px; top: 176px; }
  .person__name {
    font-family: "Cinzel", serif; font-weight: 600; font-size: 25px;
    letter-spacing: 0.5px; line-height: 1;
  }
  .person__role {
    font-family: "Cinzel", serif; font-weight: 400; font-size: 18px;
    color: var(--ink-soft); margin-top: 6px; line-height: 1;
  }
  .divider {
    position: absolute; left: 33px; right: 41px; top: 239px;
    height: 1px; background: var(--rule);
  }
  .contact-list {
    position: absolute; left: 33px; top: 253px; list-style: none;
    font-family: "PT Sans", sans-serif; font-size: 15px; color: var(--ink);
  }
  .contact-list li { display: flex; align-items: center; gap: 9px; height: 23.5px; }
  .contact-list svg { width: 13px; height: 13px; flex: none; }
  .address {
    position: absolute; right: 41px; top: 277px; text-align: right; font-style: normal;
    font-family: "PT Sans", sans-serif; font-size: 15px; line-height: 23.5px; color: var(--ink);
  }
  .website {
    position: absolute; left: 0; right: 0; top: 286px; text-align: center;
    font-family: "Cinzel", serif; font-size: 16px; letter-spacing: 5px;
  }
</style>
</head>
<body>
<main class="canvas">
  <section class="card card--front" aria-label="Business card front">
    <div class="brand"><span class="brand__mark"></span>Summit Ridge Builders</div>
    <div class="person">
      <p class="person__name">MARK HALDEN</p>
      <p class="person__role">CEO/Founder</p>
    </div>
    <div class="divider"></div>
    <ul class="contact-list">
      <li>
        <svg viewBox="0 0 13 13" aria-hidden="true"><rect x="3" y="0.5" width="7" height="12" rx="1.2" fill="none" stroke="#1a1a1a" stroke-width="1.4"/><rect x="4.3" y="2" width="4.4" height="7.5" fill="#1a1a1a"/></svg>
        541-555-0142
      </li>
      <li>
        <svg viewBox="0 0 13 13" aria-hidden="true"><rect x="0.5" y="2.5" width="12" height="8" fill="#1a1a1a"/><path d="M0.5 2.5 L6.5 7 L12.5 2.5" fill="none" stroke="#fff" stroke-width="1"/></svg>
        mhalden@summitridgebuild.com
      </li>
      <li>
        <svg viewBox="0 0 13 13" aria-hidden="true"><circle cx="6.5" cy="6.5" r="6" fill="#1a1a1a"/><ellipse cx="6.5" cy="6.5" rx="2.6" ry="6" fill="none" stroke="#fff" stroke-width="0.8"/><path d="M0.5 6.5 H12.5" stroke="#fff" stroke-width="0.8"/></svg>
        www.summitridgebuild.com
      </li>
    </ul>
    <address class="address">
      1420 Ridgeview Court<br>Pinecrest, Oregon 97488
    </address>
  </section>

  <section class="card card--back" aria-label="Business card back">
    <div class="brand"><span class="brand__mark"></span>Summit Ridge Builders</div>
    <p class="website">WWW.SUMMITRIDGEBUILD.COM</p>
  </section>
</main>
</body>
</html>
```